Logo for Internal Medicine practice

I want a logo for my Internal Medicine practice, I would like it to be with my name on it which is Lorena Benítez Prado.

I would like the business card to say the following (it is in Spanish since my practice is in Spanish):

Lorena Benítez Prado
Medicina Interna
Cel. 5587316420
lorenabenitezprado@correovela.com

Logo Text

Lorena Benítez

```html
<!DOCTYPE html>
<html lang="es">
<head>
<meta charset="utf-8">
<title>Lorena Benítez Prado · Medicina Interna · Tarjeta de presentación</title>
<link rel="stylesheet" href="https://fonts.googleapis.com/css2?family=Roboto:wght@400;700&display=swap">
<style>
  :root {
    --navy: #0e3a52;
    --teal: #1aa5b8;
    --ink-grey: #6a6f73;
    --card-white: #ffffff;
    --backdrop: #eceae6;
  }
  * { margin: 0; padding: 0; box-sizing: border-box; }
  html, body {
    width: 1200px;
    height: 841px;
    overflow: hidden;
    background: var(--backdrop);
    font-family: "Roboto", Arial, sans-serif;
  }
  .canvas {
    position: relative;
    width: 1200px;
    height: 841px;
  }
  .card {
    position: absolute;
    top: 272px;
    width: 520px;
    height: 297px;
    border-radius: 3px;
    box-shadow: 0 6px 18px rgba(0, 0, 0, 0.12);
  }
  .card--front {
    left: 50px;
    background: var(--card-white);
  }
  .card--back {
    left: 630px;
    background: var(--navy);
    display: flex;
    align-items: center;
    justify-content: center;
  }
  .brand-name {
    font-family: "Roboto", Arial, sans-serif;
    font-weight: 700;
    line-height: 1;
    white-space: nowrap;
  }
  .card--front .brand-name {
    position: absolute;
    top: 62px;
    right: 34px;
    color: var(--navy);
    font-size: 30px;
  }
  .card--back .brand-name {
    color: var(--card-white);
    font-size: 46px;
  }
  .contact {
    position: absolute;
    left: 34px;
    top: 126px;
  }
  .contact__name {
    color: var(--navy);
    font-weight: 700;
    font-size: 15px;
    text-transform: uppercase;
    letter-spacing: 0.2px;
  }
  .contact__role {
    color: var(--teal);
    font-size: 13px;
    margin-top: 2px;
  }
  .contact__address {
    color: var(--ink-grey);
    font-size: 13px;
    line-height: 1.4;
    margin-top: 14px;
    font-style: normal;
  }
  .contact__line {
    display: flex;
    align-items: center;
    gap: 6px;
    color: var(--ink-grey);
    font-size: 13px;
    line-height: 1.5;
  }
  .contact__icon {
    width: 11px;
    height: 11px;
    flex: none;
    fill: var(--navy);
  }
</style>
</head>
<body>
<main class="canvas">
  <section class="card card--front" aria-label="Frente de la tarjeta">
    <div class="contact">
      <p class="contact__name">Lorena Benítez Prado</p>
      <p class="contact__role">Medicina Interna</p>
      <address class="contact__address">48 Alder Crest Road,<br>Maple Grove, ON L6R 3K2</address>
      <p class="contact__line">
        <svg class="contact__icon" viewBox="0 0 24 24" aria-hidden="true"><path d="M6.6 10.8a15.1 15.1 0 0 0 6.6 6.6l2.2-2.2a1 1 0 0 1 1-.25 11.4 11.4 0 0 0 3.6.57 1 1 0 0 1 1 1V20a1 1 0 0 1-1 1A17 17 0 0 1 3 4a1 1 0 0 1 1-1h3.5a1 1 0 0 1 1 1c0 1.25.2 2.45.57 3.57a1 1 0 0 1-.25 1z"/></svg>
        5587316420
      </p>
      <p class="contact__line">
        <svg class="contact__icon" viewBox="0 0 24 24" aria-hidden="true"><path d="M2 5h20v14H2z M3.5 6.5 12 13l8.5-6.5" fill="none" stroke="#0e3a52" stroke-width="2.4"/></svg>
        lorenabenitezprado@correovela.com
      </p>
    </div>
    <p class="brand-name">Lorena Benítez</p>
  </section>

  <section class="card card--back" aria-label="Reverso de la tarjeta">
    <p class="brand-name">Lorena Benítez</p>
  </section>
</main>
</body>
</html>
```